電子書籍のタイトル

「窓辺に咲いた小さな灯と
心が旅をする十二の物語」

初めての出版になります。

基本デザインはお任せいたします。

デザインされる参考に添付内容の本文をお読みいください。

想定される読者の方の心に届く表紙にしたいと思います。

どうぞよろしくお願いいたします。

デザイン、文字の配置、色合いから総合的本の内容を表現されているように思いました。

この度は、表紙デザインにたくさんの方がご応募頂き誠にありがとうございました。
素晴らしい作品をたくさん頂き、正直悩みましたが、コンペという事で好みで選択させていただきました。本当に感謝申し上げます。

```html
<!DOCTYPE html>
<html lang="ja">
<head>
<meta charset="UTF-8">
<title>窓辺に咲いた小さな灯と 心が旅をする十二の物語</title>
<link rel="stylesheet" href="https://fonts.googleapis.com/css2?family=Noto+Sans+JP:wght@400;500;700;900&family=Noto+Serif+JP:wght@500;700;900&display=swap">
<style>
  :root {
    --night: #1a1208;
    --deep: #3a2a12;
    --glow: #fff4cf;
    --gold-light: #fff3b8;
    --gold: #e7b44a;
    --gold-dark: #a8661a;
    --ink-outline: #2a1a08;
    --white: #ffffff;
    --paper: #fbfaf7;
    --accent: #e05a1e;
    --accent-dark: #a8261a;
    --band: #e8672a;
    --muted: #777777;
  }
  * { margin: 0; padding: 0; box-sizing: border-box; }
  html, body { width: 750px; height: 1200px; overflow: hidden; background: var(--white); }
  .cover {
    position: relative;
    width: 750px;
    height: 1200px;
    overflow: hidden;
    font-family: "Noto Serif JP", serif;
  }
  .cover-art {
    position: absolute;
    inset: 0 0 350px 0;
    background:
      radial-gradient(ellipse 140px 260px at 50% 50%, var(--glow) 0%, rgba(255,228,150,0.85) 35%, rgba(201,138,46,0.35) 70%, transparent 100%),
      radial-gradient(circle at 85% 8%, rgba(255,220,140,0.55) 0%, transparent 22%),
      radial-gradient(circle at 12% 30%, rgba(255,200,110,0.35) 0%, transparent 25%),
      radial-gradient(circle at 90% 70%, rgba(230,170,80,0.35) 0%, transparent 28%),
      radial-gradient(ellipse at 50% 50%, var(--deep) 0%, var(--night) 80%);
  }
  .title-lead {
    position: absolute;
    top: 72px;
    left: 0;
    width: 100%;
    text-align: center;
    color: var(--white);
    font-weight: 900;
    font-size: 48px;
    line-height: 1.5;
    letter-spacing: 0.02em;
    -webkit-text-stroke: 2px var(--ink-outline);
    paint-order: stroke fill;
    text-shadow: 0 2px 6px rgba(0,0,0,0.6);
  }
  .title-main {
    position: absolute;
    top: 320px;
    left: 0;
    width: 100%;
    text-align: center;
  }
  .title-number {
    display: inline-block;
    font-weight: 900;
    font-size: 170px;
    line-height: 1;
    transform: skewX(-10deg);
    background: linear-gradient(180deg, var(--gold-light) 0%, var(--gold) 45%, var(--gold-dark) 100%);
    -webkit-background-clip: text;
    background-clip: text;
    color: transparent;
    filter: drop-shadow(0 3px 4px rgba(60,30,0,0.7));
  }
  .title-tail {
    display: block;
    margin-top: 14px;
    color: var(--white);
    font-weight: 900;
    font-size: 76px;
    line-height: 1.1;
    -webkit-text-stroke: 2px var(--ink-outline);
    paint-order: stroke fill;
    text-shadow: 0 2px 6px rgba(0,0,0,0.6);
  }
  .author {
    position: absolute;
    top: 770px;
    left: 0;
    width: 100%;
    text-align: center;
    color: var(--white);
    font-weight: 700;
    font-size: 36px;
    letter-spacing: 0.06em;
    text-shadow: 0 2px 6px rgba(0,0,0,0.7);
  }
  .author .label { margin-right: 18px; }
  .info {
    position: absolute;
    top: 850px;
    left: 0;
    width: 100%;
    height: 190px;
    background: var(--paper);
    text-align: center;
  }
  .tagline {
    margin-top: 36px;
    color: var(--accent);
    font-family: "Noto Sans JP", sans-serif;
    font-weight: 900;
    font-size: 46px;
    letter-spacing: 0.06em;
    line-height: 1.2;
  }
  .subline {
    margin-top: 12px;
    display: flex;
    align-items: center;
    justify-content: center;
    gap: 14px;
    color: var(--muted);
    font-size: 24px;
    font-weight: 500;
  }
  .subline .rule { width: 60px; height: 1px; background: var(--muted); }
  .gift-badge {
    position: absolute;
    top: 1005px;
    left: 50%;
    transform: translateX(-50%);
    width: 232px;
    height: 44px;
    background: var(--accent-dark);
    color: var(--white);
    font-family: "Noto Sans JP", sans-serif;
    font-weight: 700;
    font-size: 24px;
    line-height: 44px;
    text-align: center;
    letter-spacing: 0.06em;
    z-index: 2;
  }
  .gift-band {
    position: absolute;
    top: 1040px;
    left: 0;
    width: 100%;
    height: 160px;
    background: var(--band);
    color: var(--white);
    text-align: center;
    font-family: "Noto Sans JP", sans-serif;
  }
  .gift-note {
    margin-top: 38px;
    font-size: 27px;
    font-weight: 700;
    letter-spacing: 0.02em;
    line-height: 1.3;
  }
  .gift-title {
    margin-top: 6px;
    font-size: 46px;
    font-weight: 900;
    letter-spacing: 0.04em;
    line-height: 1.2;
  }
</style>
</head>
<body>
  <main class="cover">
    <div class="cover-art" role="img" aria-label="金色の光の粒が舞う暗い背景の中央に、まばゆい光が差し込む開いた扉"></div>

    <h1>
      <span class="title-lead">窓辺に咲いた小さな灯と<br>心が旅をする</span>
      <span class="title-main">
        <span class="title-number">十二</span>
        <span class="title-tail">の物語</span>
      </span>
    </h1>

    <p class="author"><span class="label">著</span>Sorane</p>

    <section class="info">
      <p class="tagline">心に灯をともして生きる</p>
      <p class="subline"><span class="rule"></span>窓辺から届く十二のひとしずく<span class="rule"></span></p>
    </section>

    <p class="gift-badge">読者限定プレゼント</p>

    <section class="gift-band">
      <p class="gift-note">旅のあとに読みたい、心をほどく小さな手紙</p>
      <p class="gift-title">3つのシークレットストーリー</p>
    </section>
  </main>
</body>
</html>
```